Etiketten-Design für Honiggläser
Zielgruppe
Imkerei Lindner
Wir sind eine Familienbetrieb und vertreiben hochwertigen Honig aus eigener Imkerei
Aufgabenstellung
Es werden Etiketten für Honiggläser benötigt
Es gibt drei verschiedene Größen von Gläser (siehe Anhang) und je größe einmal „Frühtracht“ und einmal „Sommertracht“
Also insgesamt 6 Etiketten
500g Frühtracht und Sommertracht
250g Frühtracht und Sommertracht
150g Frühtracht und Sommertracht

```html
<!DOCTYPE html>
<html lang="de">
<head>
<meta charset="utf-8">
<title>Imkerei Lindner – Honigetiketten</title>
<link rel="stylesheet" href="https://fonts.googleapis.com/css2?family=Playfair+Display:ital,wght@1,500&family=Mukta:wght@400;600;700&display=swap">
<style>
  :root {
    --page: #f2f2f2;
    --label: #163940;
    --honey: #e9a24b;
    --white: #ffffff;
    --badge: rgba(255, 255, 255, 0.16);
    --flora-a: #3c5a4a;
    --flora-b: #7e7196;
    --flora-c: #c9b46a;
    --flora-pink: #c9a3b8;
  }
  * { box-sizing: border-box; margin: 0; padding: 0; }
  html, body { width: 1200px; height: 694px; overflow: hidden; }
  body { background: var(--page); position: relative; font-family: "Mukta", sans-serif; }

  .label {
    position: absolute; top: 226px; height: 242px;
    background: var(--label); overflow: hidden;
  }
  .label--front-fruehtracht { left: 10px; width: 410px; }
  .label--front-sommertracht { left: 434px; width: 410px; }
  .label--back { left: 854px; width: 339px; }

  .flora { position: absolute; top: 0; bottom: 0; opacity: .75; }
  .flora--left {
    left: 0; width: 125px;
    background: linear-gradient(100deg, var(--flora-a) 0%, var(--flora-b) 35%, var(--flora-c) 65%, rgba(22,57,64,0) 100%);
  }
  .flora--right {
    right: 0; width: 135px;
    background: linear-gradient(260deg, var(--flora-a) 0%, var(--flora-c) 35%, var(--flora-b) 65%, rgba(22,57,64,0) 100%);
  }

  .brand-tab {
    position: absolute; top: 0; left: 126px; width: 159px; height: 85px;
    background: var(--white); border-radius: 0 0 14px 14px;
    display: flex; align-items: center; justify-content: center; gap: 6px;
  }
  .brand-tab__mark { width: 9px; height: 9px; background: var(--honey); border-radius: 50%; }
  .brand-tab__name {
    font-family: "Mukta", sans-serif; font-weight: 700; font-size: 19px;
    color: var(--honey); letter-spacing: .5px;
  }

  .product-title {
    position: absolute; left: 0; right: 0; text-align: center;
    font-family: "Playfair Display", serif; font-style: italic; font-weight: 500;
    color: var(--honey); line-height: 1;
  }
  .product-title--kind { top: 100px; font-size: 40px; }
  .product-title--variety { top: 150px; font-size: 35px; }

  .weight-tab {
    position: absolute; bottom: 0; left: 167px; width: 76px; height: 37px;
    background: var(--white); border-radius: 8px 8px 0 0;
    color: var(--honey); font-weight: 700; font-size: 20px;
    display: flex; align-items: center; justify-content: center;
  }

  .flora-band {
    position: absolute; left: 0; right: 0; opacity: .8;
    background: linear-gradient(90deg, var(--flora-pink), var(--flora-c), var(--flora-b), var(--flora-pink), var(--flora-c), var(--flora-b), var(--flora-pink));
  }
  .flora-band--top { top: 0; height: 28px; }
  .flora-band--bottom { bottom: 0; height: 24px; }

  .cert-badge {
    position: absolute; left: 26px; width: 80px; height: 60px;
    background: var(--badge); border-radius: 6px;
  }
  .cert-badge--organic { top: 37px; }
  .cert-badge--national { top: 132px; }
  .cert-code {
    position: absolute; left: 20px; top: 102px; width: 92px; text-align: center;
    color: var(--white); font-size: 11px; line-height: 1;
  }

  .info {
    position: absolute; left: 121px; top: 33px; width: 215px;
    color: var(--white); font-size: 11.5px; line-height: 12.6px;
  }
  .info__brand { font-weight: 600; margin-bottom: 14px; }
  .info__net { margin: 6px 0; }
  .info__date-field {
    width: 148px; height: 29px; background: var(--white); margin: 4px 0 9px;
  }
</style>
</head>
<body>

  <section class="label label--front-fruehtracht">
    <div class="flora flora--left" role="img" aria-label="Botanische Illustration: Glockenblumen, Vergissmeinnicht und Brombeeren"></div>
    <div class="flora flora--right" role="img" aria-label="Botanische Illustration: Akelei, Vergissmeinnicht und Brombeeren"></div>
    <div class="brand-tab"><span class="brand-tab__mark"></span><span class="brand-tab__name">Imkerei Lindner</span></div>
    <h2 class="product-title product-title--kind">Honig</h2>
    <p class="product-title product-title--variety">Frühtracht</p>
    <div class="weight-tab">500g</div>
  </section>

  <section class="label label--front-sommertracht">
    <div class="flora flora--left" role="img" aria-label="Botanische Illustration: gelbe Mohnblüten und Stiefmütterchen"></div>
    <div class="flora flora--right" role="img" aria-label="Botanische Illustration: gelbe Blüten, Knospen und Schleifenband"></div>
    <div class="brand-tab"><span class="brand-tab__mark"></span><span class="brand-tab__name">Imkerei Lindner</span></div>
    <h2 class="product-title product-title--kind">Honig</h2>
    <p class="product-title product-title--variety">Sommertracht</p>
    <div class="weight-tab">500g</div>
  </section>

  <section class="label label--back">
    <div class="flora-band flora-band--top" role="img" aria-label="Blütenbordüre mit rosa, gelben und violetten Blüten"></div>
    <div class="cert-badge cert-badge--organic" role="img" aria-label="Platz für Bio-Zertifizierungszeichen"></div>
    <p class="cert-code">AT-BIO-xxx</p>
    <div class="cert-badge cert-badge--national" role="img" aria-label="Platz für Bio-Siegel"></div>
    <div class="info">
      <p class="info__brand">Imkerei Lindner</p>
      <p>Heideweg 7, 31708 Blumenau<br>Info@imkerei-lindner.de<br>www.imkerei-lindner.de</p>
      <p class="info__net">Nettofüllmenge: 500g</p>
      <p>Lagerbedingungen,<br>- dunkel, kühl und trocken<br>Mindesthaltbarkeitsdatum,</p>
      <div class="info__date-field"></div>
      <p>Deutscher Honig aus eigener Imkerei</p>
    </div>
    <div class="flora-band flora-band--bottom" role="img" aria-label="Blütenbordüre mit rosa, gelben und violetten Blüten"></div>
  </section>

</body>
</html>
```